Refresh of The Marston Collective business card

Update business card design using existing primary logo. Names, numbers, etc. are too hard to read on current design.

Target Market(s)

We are a CPA firm.

Industry/Entity Type

Accountant

Contact Information for Business Card

update current card

Colors
0355a3
3176b5
85acd3
0792cd

Requirements
Must have
• Easier to read phone numbers and names
• Use existing logo
Nice to have
• We love our color scheme and current TMC logo. But the names and phone numbers are too small and card just look old and stale.

```html
<!DOCTYPE html>
<html lang="en">
<head>
<meta charset="utf-8">
<title>The Marston Collective – Business Card</title>
<link rel="stylesheet" href="https://fonts.googleapis.com/css2?family=Cormorant+Garamond:wght@600&family=Arimo:wght@400;500&display=swap">
<style>
  :root {
    --navy: #0355a3;
    --mid-blue: #3176b5;
    --pale-blue: #85acd3;
    --sky: #0792cd;
    --band: #1d3f8a;
    --band-grey: #4a4d52;
    --ink: #2f3237;
    --paper: #ffffff;
    --paper-shade: #e4e6e8;
    --stage: #ece9e4;
  }
  html, body {
    margin: 0;
    width: 1200px;
    height: 1023px;
    overflow: hidden;
    background: var(--stage);
  }
  .stage {
    position: relative;
    width: 1200px;
    height: 1023px;
  }
  .card {
    position: absolute;
    left: 250px;
    width: 700px;
    height: 400px;
    border-radius: 22px;
    overflow: hidden;
    box-shadow: 0 10px 28px rgba(0,0,0,.18);
  }
  /* front */
  .card-front {
    top: 70px;
    background: linear-gradient(180deg, var(--paper) 0%, var(--paper) 45%, var(--paper-shade) 100%);
  }
  .front-brand {
    position: absolute;
    left: 40px;
    top: 42px;
    display: flex;
    align-items: center;
    gap: 18px;
  }
  .brand-dot {
    width: 78px;
    height: 78px;
    border-radius: 50%;
    background: var(--navy);
    flex: none;
  }
  .brand-name {
    font-family: "Cormorant Garamond", serif;
    font-weight: 600;
    font-size: 38px;
    line-height: 1;
    color: var(--navy);
  }
  .brand-tagline {
    margin-top: 8px;
    font-family: "Arimo", sans-serif;
    font-size: 9px;
    letter-spacing: 2.6px;
    text-transform: uppercase;
    color: var(--navy);
  }
  .rule {
    position: absolute;
    left: 40px;
    right: 0;
    top: 150px;
    height: 1px;
    background: #8a9099;
  }
  .rule-drop {
    position: absolute;
    left: 140px;
    top: 150px;
    width: 1px;
    height: 212px;
    background: #8a9099;
  }
  .holder-name {
    position: absolute;
    right: 70px;
    top: 120px;
    padding: 0 12px;
    background: var(--paper);
    font-family: "Arimo", sans-serif;
    font-size: 22px;
    letter-spacing: .5px;
    color: var(--navy);
  }
  .contact {
    position: absolute;
    left: 170px;
    top: 190px;
    font-family: "Arimo", sans-serif;
    font-size: 17px;
    line-height: 26px;
    color: var(--ink);
  }
  .contact p { margin: 0; }
  .contact-line {
    display: flex;
    align-items: center;
    gap: 10px;
  }
  .contact-line svg { width: 14px; height: 14px; flex: none; }
  .front-band {
    position: absolute;
    left: 0;
    right: 0;
    bottom: 0;
    height: 36px;
    display: flex;
  }
  .front-band .blue { flex: 1; background: var(--band); }
  .front-band .grey { width: 90px; background: var(--band-grey); }
  /* back */
  .card-back {
    top: 553px;
    background: radial-gradient(ellipse at 60% 40%, var(--sky) 0%, var(--mid-blue) 35%, var(--navy) 70%, #06367a 100%);
  }
  .back-brand {
    position: absolute;
    left: 0;
    right: 0;
    top: 110px;
    display: flex;
    align-items: center;
    justify-content: center;
    gap: 22px;
  }
  .back-brand .brand-dot {
    width: 104px;
    height: 104px;
    background: var(--paper);
  }
  .back-brand .brand-name { color: var(--paper); font-size: 46px; }
  .back-brand .brand-tagline { color: var(--paper); font-size: 10px; }
  .back-rule {
    height: 1px;
    background: var(--pale-blue);
    margin-top: 8px;
  }
  .website {
    position: absolute;
    left: 0;
    right: 0;
    bottom: 62px;
    text-align: center;
    font-family: "Arimo", sans-serif;
    font-size: 19px;
    letter-spacing: .5px;
    color: var(--paper);
  }
</style>
</head>
<body>
<main class="stage">
  <section class="card card-front" aria-label="Business card front">
    <div class="front-brand">
      <div class="brand-dot"></div>
      <div>
        <div class="brand-name">The Marston Collective</div>
        <div class="brand-tagline">Certified Public Accountants</div>
      </div>
    </div>
    <div class="rule"></div>
    <div class="rule-drop"></div>
    <div class="holder-name">DANIEL R. MARSTON, CPA</div>
    <div class="contact">
      <p>312 Lakeview Ave. Suite 104</p>
      <p>Winter Park, Florida 32789</p>
      <p class="contact-line">
        <svg viewBox="0 0 14 14" aria-hidden="true"><circle cx="7" cy="7" r="6" fill="none" stroke="#2f3237" stroke-width="1.4"/><path d="M4.5 4.5c0 3 2 5 5 5l.6-1.4-1.6-.8-.7.7c-.9-.4-1.5-1-1.9-1.9l.7-.7-.8-1.6z" fill="#2f3237"/></svg>
        407 555 0142
      </p>
      <p class="contact-line">
        <svg viewBox="0 0 14 14" aria-hidden="true"><rect x="2" y="5" width="10" height="7" rx="1" fill="#2f3237"/><rect x="4" y="1.5" width="6" height="4" fill="none" stroke="#2f3237" stroke-width="1.2"/></svg>
        407 555 0143
      </p>
      <p class="contact-line">
        <svg viewBox="0 0 14 14" aria-hidden="true"><rect x="3.5" y="1" width="7" height="12" rx="1" fill="none" stroke="#2f3237" stroke-width="1.3"/></svg>
        407 555 0188
      </p>
      <p class="contact-line">
        <svg viewBox="0 0 14 14" aria-hidden="true"><rect x="1" y="3" width="12" height="8" fill="#2f3237"/><path d="M1 3l6 5 6-5" fill="none" stroke="#ffffff" stroke-width="1.1"/></svg>
        dan@marstoncollective.com
      </p>
    </div>
    <div class="front-band"><div class="blue"></div><div class="grey"></div></div>
  </section>

  <section class="card card-back" aria-label="Business card back">
    <div class="back-brand">
      <div class="brand-dot"></div>
      <div>
        <div class="brand-name">The Marston Collective</div>
        <div class="back-rule"></div>
        <div class="brand-tagline">Certified Public Accountants</div>
      </div>
    </div>
    <div class="website">www.marstoncollective.com</div>
  </section>
</main>
</body>
</html>
```